Bag Design For Frozen Prawns

Basically we need a design for a plastic bag that we have packed in Vietnam. I have attached a copy of our logo a picture of a bag I like.
As you can see it is simple clean and fresh.

Target Market(s)

Chefs

Industry/Entity Type

Plastic

```html
<!DOCTYPE html>
<html lang="en">
<head>
<meta charset="utf-8">
<title>Tidepantry Raw Shrimp Bag</title>
<link rel="stylesheet" href="https://fonts.googleapis.com/css2?family=Open+Sans:wght@400;700&family=Arimo:wght@400;700&display=swap">
<style>
  :root {
    --bag-black: #000000;
    --fresh-green: #a3d62a;
    --leaf-green: #8cc63f;
    --label-green: #8dc63f;
    --ink-white: #ffffff;
    --ink-black: #111111;
    --brand-blue: #2aa7d8;
    --callout-red: #d9261c;
    --shrimp-light: #e8dcd6;
    --shrimp-mid: #c9b8b2;
    --shrimp-shade: #8f8f94;
  }
  * { margin: 0; padding: 0; box-sizing: border-box; }
  html, body { width: 1200px; height: 848px; overflow: hidden; background: var(--bag-black); }
  .bag {
    position: relative;
    width: 1200px;
    height: 848px;
    overflow: hidden;
    background: var(--bag-black);
    font-family: "Open Sans", Arial, sans-serif;
    color: var(--ink-white);
  }
  .bag-shapes { position: absolute; inset: 0; }
  .panel-label {
    position: absolute;
    top: 14px;
    font-family: "Arimo", Arial, sans-serif;
    font-size: 38px;
    letter-spacing: 1px;
  }
  .panel-label--front { left: 389px; }
  .panel-label--back { left: 677px; }

  .brand {
    position: absolute;
    left: 48px;
    top: 112px;
    display: flex;
    align-items: center;
    gap: 14px;
  }
  .brand-dot {
    width: 46px; height: 46px;
    border-radius: 50%;
    background: var(--brand-blue);
  }
  .brand-name {
    font-size: 44px;
    font-weight: 700;
    color: var(--brand-blue);
    letter-spacing: 1px;
  }

  .product-name {
    position: absolute;
    left: 50px;
    top: 218px;
    font-size: 64px;
    line-height: 84px;
    font-weight: 400;
  }
  .net-weight {
    position: absolute;
    left: 50px;
    top: 802px;
    font-size: 15px;
  }

  .nutrition {
    position: absolute;
    left: 617px;
    top: 102px;
    width: 226px;
    height: 323px;
    border: 1px solid var(--label-green);
    padding: 2px 3px;
    font-family: "Arimo", Arial, sans-serif;
    color: var(--label-green);
    font-size: 9px;
    line-height: 1.2;
  }
  .nutrition-title { font-size: 23px; letter-spacing: 2.4px; line-height: 24px; }
  .nutrition-row { display: flex; justify-content: space-between; border-top: 1px solid var(--label-green); padding: 1px 0; }
  .nutrition-row--thick { border-top-width: 5px; }
  .nutrition-row--mid { border-top-width: 3px; }
  .nutrition-row--indent { padding-left: 14px; }
  .nutrition-row b { font-weight: 700; }
  .nutrition-small { font-size: 7px; }
  .nutrition-note { font-size: 6.5px; border-top: 1px solid var(--label-green); padding: 1px 0; line-height: 1.25; }
  .nutrition-table { width: 100%; font-size: 6.5px; border-collapse: collapse; border-top: 1px solid var(--label-green); }
  .nutrition-table td { padding: 0; line-height: 1.3; }

  .recipes {
    position: absolute;
    left: 901px;
    top: 196px;
    width: 262px;
    color: var(--ink-black);
  }
  .recipes-title { font-size: 20px; font-weight: 400; margin-bottom: 6px; }
  .recipes p { font-size: 8.6px; line-height: 12px; margin-bottom: 12px; }

  .photo-callout {
    position: absolute;
    top: 506px;
    width: 280px;
    text-align: center;
    font-family: "Arimo", Arial, sans-serif;
    font-size: 34px;
    line-height: 47px;
    color: var(--callout-red);
    text-shadow: 0 0 2px #000, 0 0 2px #000, 0 0 3px #000;
  }
  .photo-callout--front { left: 257px; }
  .photo-callout--back { left: 655px; }
</style>
</head>
<body>
<main class="bag">
  <svg class="bag-shapes" width="1200" height="848" viewBox="0 0 1200 848" aria-hidden="false">
    <defs>
      <linearGradient id="swoosh-fill" x1="0" y1="1" x2="1" y2="0">
        <stop offset="0" stop-color="#8cc63f"/>
        <stop offset="1" stop-color="#4f7a1e"/>
      </linearGradient>
      <radialGradient id="shrimp-fill" cx="0.5" cy="0.5" r="0.6">
        <stop offset="0" stop-color="#d8ccc8"/>
        <stop offset="0.6" stop-color="#c2b4b0"/>
        <stop offset="1" stop-color="#9a9aa0"/>
      </radialGradient>
    </defs>
    <path class="green-panel" d="M872 0 H1200 V556 Q1090 625 1012 656 Q905 580 872 440 Z" fill="var(--fresh-green)"/>
    <path class="green-swoosh" d="M0 500 Q230 395 505 372 Q260 405 0 578 Z" fill="url(#swoosh-fill)"/>
    <ellipse class="product-photo" role="img" aria-label="Photo of raw peeled shrimp, or a clear window showing the product"
             cx="596" cy="616" rx="434" ry="172" fill="url(#shrimp-fill)"/>
    <line class="fold-line" x1="596" y1="0" x2="596" y2="848" stroke="var(--ink-white)" stroke-width="2" stroke-dasharray="9 8"/>
  </svg>

  <div class="panel-label panel-label--front">FRONT</div>
  <div class="panel-label panel-label--back">BACK</div>

  <div class="brand">
    <span class="brand-dot"></span>
    <span class="brand-name">TIDEPANTRY</span>
  </div>

  <h1 class="product-name">Raw<br>Shrimp</h1>
  <div class="net-weight">NET WT. 16OZ. (1 LB) 454g</div>

  <section class="nutrition">
    <div class="nutrition-title">Nutrition Facts</div>
    <div class="nutrition-small">Serving Size 458</div>
    <div class="nutrition-row nutrition-row--thick nutrition-small"><b>Amount Per Serving</b></div>
    <div class="nutrition-row"><span><b>Calories</b> 600</span><span>Calories from Fat 350</span></div>
    <div class="nutrition-row nutrition-row--mid nutrition-small" style="justify-content:flex-end"><b>% Daily Values*</b></div>
    <div class="nutrition-row"><span><b>Total Fat</b> 39g</span><b>60%</b></div>
    <div class="nutrition-row nutrition-row--indent"><span>Saturated Fat 5g</span><b>25%</b></div>
    <div class="nutrition-row nutrition-row--indent"><span>Trans Fat 0g</span></div>
    <div class="nutrition-row"><span><b>Cholesterol</b> 0mg</span><b>0%</b></div>
    <div class="nutrition-row"><span><b>Sodium</b> 30mg</span><b>1%</b></div>
    <div class="nutrition-row"><span><b>Total Carbohydrate</b> 83g</span><b>28%</b></div>
    <div class="nutrition-row nutrition-row--indent"><span>Dietary Fiber 17g</span><b>68%</b></div>
    <div class="nutrition-row nutrition-row--indent"><span>Sugars 26g</span></div>
    <div class="nutrition-row"><span><b>Protein</b> 16g</span><b>32%</b></div>
    <div class="nutrition-row nutrition-row--thick"><span>Vitamin A 120%</span><span>•</span><span>Vitamin C 220%</span></div>
    <div class="nutrition-row"><span>Calcium 15%</span><span>•</span><span>Iron 25%</span></div>
    <div class="nutrition-note">* Percent Daily Values are based on a 2,000 calorie diet. Your Daily Values may be higher or lower depending on your calorie needs.</div>
    <table class="nutrition-table">
      <tr><td></td><td>Calories</td><td>2,000</td><td>2,500</td></tr>
      <tr><td>Total Fat</td><td>Less than</td><td>65g</td><td>80g</td></tr>
      <tr><td>&nbsp;Sat Fat</td><td>Less than</td><td>20g</td><td>25g</td></tr>
      <tr><td>Cholesterol</td><td>Less than</td><td>300mg</td><td>300mg</td></tr>
      <tr><td>Sodium</td><td>Less than</td><td>2400mg</td><td>2400mg</td></tr>
      <tr><td>Total Carbohydrate</td><td></td><td>300g</td><td>375g</td></tr>
      <tr><td>&nbsp;Dietary Fiber</td><td></td><td>25g</td><td>30g</td></tr>
    </table>
  </section>

  <section class="recipes">
    <h2 class="recipes-title">Recipes</h2>
    <p>Lorem ipsum dolor sit amet, consectetur adipiscing elit.<br>Etiam vehicula diam iaculis odio tempus, ac dignissim purus placerat.<br>Sed ut purus lacinia, viverra diam in, rhoncus metus.</p>
    <p>Pellentesque elementum lectus non fringilla finibus.<br>Etiam pretium neque at molestie imperdiet.<br>Curabitur sed turpis convallis est vulputate sodales ac nec urna.</p>
    <p>Donec congue dui ac molestie vestibulum.<br>Proin laoreet mi id massa malesuada, ullamcorper condimentum orci viverra.</p>
  </section>

  <div class="photo-callout photo-callout--front">Relevant stock food image or Transparent plastic</div>
  <div class="photo-callout photo-callout--back">Relevant stock food image or Transparent plastic</div>
</main>
</body>
</html>
```